Lumora Education - new College Consulting company in San Francisco needs a flyer design

We need a logo design for a new college admissions consulting business in San Francisco Bay Area and San Jose called 'Lumora Education'. We plan to develop tailor-made strategies for each students dreams and aspirations and will help provide them with online classes and in-person consulting starting Summer 2022.
Lumora Education plans on providing a free first time consulting to attract clients and grow our client base from there.
Lumora Education has a small team of consultants who have degrees from Economics/Business, Biology, and Computer Science who can provide tailored guidance to meet student and parent expectations and spend the time to walk them throughout the process.
Please refer to attached logos for the company and to create a flyer.
Target Market(s)
Competitive College Consulting
Industry/Entity Type
Education Consulting
Look and feel

```html
<!DOCTYPE html>
<html lang="en">
<head>
<meta charset="utf-8">
<title>Lumora Education – College Admission Flyer</title>
<link rel="stylesheet" href="https://fonts.googleapis.com/css2?family=Montserrat:wght@700;800;900&family=Oswald:wght@500;600&family=Poppins:wght@400;500;600;700&family=Crimson+Text:wght@400&display=swap">
<style>
:root{
  --pink:#f2847b;
  --pink-deep:#e06a62;
  --red:#d40000;
  --ink:#242424;
  --dark:#2a2a2a;
  --panel:#ececec;
  --white:#ffffff;
  --page:#f4f4f4;
}
*{margin:0;padding:0;box-sizing:border-box}
html,body{width:1200px;height:2948px;overflow:hidden;background:var(--page)}
.flyer{
  position:absolute;left:61px;top:776px;width:842px;height:1090px;
  transform:scale(1.28);transform-origin:0 0;
  background:var(--white);overflow:hidden;
  box-shadow:0 4px 14px rgba(0,0,0,.18);
  font-family:"Poppins",sans-serif;color:var(--ink);
}
.abs{position:absolute}
.hero-photo{left:340px;top:0;width:502px;height:415px;
  background:linear-gradient(120deg,#d9d2c8 0%,#b7a89a 35%,#8e7c70 60%,#c8b9ae 100%)}
.hero-shapes{left:0;top:0;width:842px;height:420px}
.brand{left:37px;top:46px;width:270px;text-align:right}
.brand-name{font-family:"Poppins",sans-serif;font-weight:500;font-size:17px;color:#4a2323;line-height:22px;padding-right:64px}
.brand-tag{font-family:"Crimson Text",serif;font-size:16px;color:#4a2323;line-height:20px;padding-right:64px}
.brand-dot{position:absolute;right:14px;top:8px;width:38px;height:38px;border-radius:50%;background:var(--ink)}
.kicker{left:38px;top:120px;font-family:"Oswald",sans-serif;font-weight:600;font-size:34px;line-height:42px;letter-spacing:-.5px}
.kicker em{font-style:normal;color:var(--pink)}
.title-main{left:38px;top:190px;font-family:"Montserrat",sans-serif;font-weight:900;font-size:74px;line-height:80px;color:var(--ink);letter-spacing:1px}
.title-sub{left:40px;top:270px;font-family:"Montserrat",sans-serif;font-weight:800;font-size:56px;line-height:60px;color:var(--white);letter-spacing:1px}
.city{left:45px;top:348px;display:flex;align-items:center;gap:22px;color:var(--white);font-size:37px;line-height:48px}
.regions{left:40px;top:414px;font-size:35px;font-weight:600;line-height:46px}
.regions span{color:var(--pink)}
.intro{left:42px;top:470px;width:400px;font-size:13.6px;font-weight:600;line-height:21.5px}
.intro span{color:var(--pink-deep)}
.process{left:40px;top:614px;width:355px;height:410px;background:var(--panel)}
.process-title{left:50px;top:628px;width:357px;height:44px}
.process-title h2{position:absolute;left:22px;top:6px;font-size:23px;font-weight:500;line-height:32px;color:var(--ink)}
.process-list{left:68px;top:688px;width:318px;list-style:none}
.process-list li{position:relative;padding-left:26px;font-size:12px;line-height:17px;margin-bottom:11px;color:#333}
.process-list li b{font-weight:600}
.process-list li svg{position:absolute;left:0;top:3px}
.free{left:466px;top:432px;width:329px;height:73px;background:var(--red);border-radius:0 0 10px 10px;
  color:var(--white);font-family:"Montserrat",sans-serif;font-weight:900;font-size:76px;line-height:73px;text-align:center;letter-spacing:2px}
.consult-icon{left:472px;top:510px;width:86px;height:82px;background:#dedede}
.first-time{left:565px;top:514px;font-family:"Montserrat",sans-serif;font-weight:900;font-size:40px;line-height:44px;color:var(--red);letter-spacing:-.5px}
.consulting{left:566px;top:556px;font-family:"Montserrat",sans-serif;font-weight:800;font-size:34px;line-height:40px;color:var(--ink)}
.offer{left:458px;top:608px;width:338px;height:204px;border:2px solid var(--ink)}
.offer-banner{left:478px;top:606px;width:298px;height:132px}
.offer-text{left:478px;top:622px;width:298px;text-align:center;color:var(--white)}
.offer-text .l1{font-size:15px;font-weight:600;line-height:20px}
.offer-text .l2{font-size:19px;font-weight:500;line-height:26px}
.offer-text .l3{font-size:33px;font-weight:500;line-height:40px;color:var(--pink)}
.offer-note{left:458px;top:740px;width:338px;text-align:center}
.offer-note .n1{font-size:20px;font-weight:600;line-height:28px}
.offer-note .n2{font-family:"Montserrat",sans-serif;font-size:31px;font-weight:800;line-height:40px}
.study-photo{left:458px;top:825px;width:334px;height:178px;
  background:linear-gradient(110deg,#6b6f73 0%,#a9adb1 40%,#e7e4df 70%,#c9c2b8 100%)}
.footer-shape{left:0;top:1030px;width:842px;height:60px}
.apply{left:38px;top:1041px;font-size:23px;line-height:40px;color:var(--ink)}
.apply b{font-weight:700}
.phone{left:372px;top:1040px;display:flex;align-items:center;gap:6px;font-size:27px;font-weight:600;line-height:40px}
.contact{left:612px;top:1037px;font-size:13px;line-height:20px}
.contact div{display:flex;align-items:center;gap:10px}
</style>
</head>
<body>
<main class="flyer">
  <div class="abs hero-photo" role="img" aria-label="Photo of four smiling college students holding books"></div>
  <svg class="abs hero-shapes" viewBox="0 0 842 420" aria-hidden="true">
    <polygon points="0,0 352,0 455,415 0,415" fill="#ffffff"/>
    <polygon points="352,0 366,0 470,415 456,415" fill="#1e1e1e"/>
    <polygon points="0,172 414,172 455,340 0,340" fill="#f2847b"/>
    <polygon points="0,340 455,340 470,403 0,403" fill="#2a2a2a"/>
  </svg>

  <div class="abs brand">
    <div class="brand-name">Lumora Education</div>
    <div class="brand-tag">Learning is a phenomenom</div>
    <span class="brand-dot"></span>
  </div>

  <div class="abs kicker">NEW COLLAGE <em>ADDMISSION</em></div>
  <div class="abs title-main">LUMORA</div>
  <div class="abs title-sub">EDUCATION</div>
  <div class="abs city">
    <svg width="30" height="36" viewBox="0 0 30 36" aria-hidden="true">
      <path d="M15 2C8.5 2 4 7 4 13c0 8 11 19 11 19s11-11 11-19C26 7 21.5 2 15 2z" fill="none" stroke="#f2847b" stroke-width="3"/>
      <circle cx="15" cy="13" r="4" fill="none" stroke="#f2847b" stroke-width="3"/>
      <ellipse cx="15" cy="33" rx="12" ry="2.5" fill="none" stroke="#f2847b" stroke-width="2"/>
    </svg>
    <span>in San Francisco</span>
  </div>

  <div class="abs regions"><span>Bay Area</span> and <span>San Jose</span></div>
  <p class="abs intro">Lumora Education has a small team of consultants who have degrees from <span>Economics/Business, Biology, and Computer Science</span> who can provide tailored guidance to meet student and parent expectations and spend the time to walk them throughout the process.</p>

  <div class="abs process"></div>
  <div class="abs process-title">
    <svg width="357" height="44" viewBox="0 0 357 44" aria-hidden="true">
      <defs><linearGradient id="band" x1="0" x2="1"><stop offset="0" stop-color="#f08078"/><stop offset="1" stop-color="#f6a49c"/></linearGradient></defs>
      <rect x="0" y="0" width="357" height="38" fill="url(#band)"/>
      <polygon points="345,38 357,38 345,44" fill="#b55a53"/>
    </svg>
    <h2>Lumora Education Process</h2>
  </div>
  <ul class="abs process-list">
    <li><svg width="12" height="12" viewBox="0 0 12 12"><circle cx="6" cy="6" r="6" fill="#f2847b"/><path d="M3.3 6.2l1.8 1.8 3.6-3.8" stroke="#fff" stroke-width="1.4" fill="none"/></svg>We plan to develop tailor-made strategies for each students dreams</li>
    <li><svg width="12" height="12" viewBox="0 0 12 12"><circle cx="6" cy="6" r="6" fill="#f2847b"/><path d="M3.3 6.2l1.8 1.8 3.6-3.8" stroke="#fff" stroke-width="1.4" fill="none"/></svg>Aspirations and will help provide them with online classe</li>
    <li><svg width="12" height="12" viewBox="0 0 12 12"><circle cx="6" cy="6" r="6" fill="#f2847b"/><path d="M3.3 6.2l1.8 1.8 3.6-3.8" stroke="#fff" stroke-width="1.4" fill="none"/></svg>In-person consulting</li>
    <li><svg width="12" height="12" viewBox="0 0 12 12"><circle cx="6" cy="6" r="6" fill="#f2847b"/><path d="M3.3 6.2l1.8 1.8 3.6-3.8" stroke="#fff" stroke-width="1.4" fill="none"/></svg>Lumora Education plans on providing a free first time consulting</li>
    <li><svg width="12" height="12" viewBox="0 0 12 12"><circle cx="6" cy="6" r="6" fill="#f2847b"/><path d="M3.3 6.2l1.8 1.8 3.6-3.8" stroke="#fff" stroke-width="1.4" fill="none"/></svg>Lumora Education has a small team of consultants who have degrees from <b>Economics/Business, Biology, and Computer Science</b></li>
    <li><svg width="12" height="12" viewBox="0 0 12 12"><circle cx="6" cy="6" r="6" fill="#f2847b"/><path d="M3.3 6.2l1.8 1.8 3.6-3.8" stroke="#fff" stroke-width="1.4" fill="none"/></svg>who can provide tailored guidance to meet student and parent expectations and spend the time to walk them throughout the process.</li>
  </ul>

  <div class="abs free">FREE</div>
  <div class="abs consult-icon" role="img" aria-label="Icon of a consultant seated at a desk"></div>
  <div class="abs first-time">FIRST TIME</div>
  <div class="abs consulting">CONSULTING</div>

  <div class="abs offer"></div>
  <svg class="abs offer-banner" viewBox="0 0 298 132" aria-hidden="true">
    <polygon points="0,0 298,0 298,95 149,130 0,95" fill="#2a2a2a"/>
  </svg>
  <div class="abs offer-text">
    <div class="l1">IN-PERSON</div>
    <div class="l2">CONSULTING STARTING</div>
    <div class="l3">SUMMER 2022</div>
  </div>
  <div class="abs offer-note">
    <div class="n1">Will help provide them with</div>
    <div class="n2">ONLINE CLASSES</div>
  </div>

  <div class="abs study-photo" role="img" aria-label="Photo of a student taking notes during an online video class on a laptop"></div>

  <svg class="abs footer-shape" viewBox="0 0 842 60" aria-hidden="true">
    <polygon points="0,5 352,5 372,50 0,50" fill="#f2847b"/>
    <rect x="0" y="50" width="842" height="10" fill="#f2847b"/>
  </svg>
  <div class="abs apply"><b>APPLY NOW</b> FOR CLASSES</div>
  <div class="abs phone">
    <svg width="17" height="17" viewBox="0 0 24 24" aria-hidden="true"><path d="M6.6 10.8a15 15 0 006.6 6.6l2.2-2.2a1 1 0 011-.25 11 11 0 003.5.56 1 1 0 011 1V20a1 1 0 01-1 1A17 17 0 013 4a1 1 0 011-1h3.5a1 1 0 011 1 11 11 0 00.56 3.5 1 1 0 01-.25 1z" fill="#f2847b"/></svg>
    <span>415-555-0142</span>
  </div>
  <div class="abs contact">
    <div><svg width="15" height="13" viewBox="0 0 16 14" aria-hidden="true"><rect x="1" y="2" width="14" height="10" fill="none" stroke="#f2847b" stroke-width="1.6"/><path d="M1 2l7 6 7-6" fill="none" stroke="#f2847b" stroke-width="1.6"/></svg>info@lumoraeducation.com</div>
    <div><svg width="15" height="15" viewBox="0 0 16 16" aria-hidden="true"><circle cx="8" cy="8" r="6.5" fill="none" stroke="#f2847b" stroke-width="1.4"/><ellipse cx="8" cy="8" rx="3" ry="6.5" fill="none" stroke="#f2847b" stroke-width="1.2"/><path d="M1.5 8h13" stroke="#f2847b" stroke-width="1.2"/></svg>www.lumoraeducation.com</div>
  </div>
</main>
</body>
</html>
```